social interest sharing site needs a web site design

we need a web site design for a social web platform.
the site is one page(main page), that is split into 3 sections
each section is a different color(red,green and blue)
and a user can choose to share each of the sections.
any section/color will contain boxes , each box can contain different media types.

the media types:
* list of URLS
* list of articles including title + image + description
* list of videos
* thumbnails of images
* calender
* list of emails

the main content will look like corkboardly layout
multiple boxes each box can contain different type of content as described above

each color is a different tab
each tab will have layout like corkboardly
Updates

please read the last description update.
and i uploaded an image that can explain the requirements better

thanks
Oren
 

Industry/Entity Type

Media

```html
<!DOCTYPE html>
<html lang="en">
<head>
<meta charset="utf-8">
<title>Kornr.me – My Home Page</title>
<link href="https://fonts.googleapis.com/css2?family=Arimo:wght@400;700&display=swap" rel="stylesheet">
<style>
:root{
  --ink:#1d1d1d;
  --muted:#555;
  --header-bg:#f3f3f3;
  --page-bg:#fdf8ea;
  --red:#ff3a3f;
  --red-light:#ff7a7a;
  --green:#00b36b;
  --green-light:#00d1b0;
  --blue:#0a86d6;
  --blue-light:#1aa7ef;
  --bar-dark:#111;
  --bar-mid:#3a3a3a;
  --card-border:#dcdcdc;
  --icon:#333;
}
*{box-sizing:border-box;margin:0;padding:0}
html,body{width:1132px;height:1200px;overflow:hidden}
body{font-family:"Arimo",Arial,sans-serif;background:var(--page-bg);color:var(--ink);position:relative}

.top-stripe{position:absolute;top:0;left:0;width:1132px;height:3px;background:linear-gradient(90deg,var(--red-light) 0 33%,var(--green-light) 33% 66%,var(--blue-light) 66%)}
.site-header{position:absolute;top:3px;left:0;width:1132px;height:186px;background:var(--header-bg);border-bottom:1px solid #c9c3b4}

.brand{position:absolute;left:74px;top:43px;height:62px;border-left:1px solid #888;padding-left:14px;display:flex;align-items:center}
.brand-name{font-size:40px;font-weight:700;letter-spacing:-2px;color:var(--ink)}

.section-tabs{position:absolute;top:48px;left:322px;display:flex;gap:3px}
.section-tab{height:46px;display:flex;align-items:center;justify-content:center;color:#fff;font-size:16px;border-radius:5px 5px 0 0}
.section-tab.red{width:192px;background:linear-gradient(180deg,var(--red),var(--red-light))}
.section-tab.green{width:221px;background:linear-gradient(180deg,var(--green),var(--green-light))}
.section-tab.blue{width:193px;background:linear-gradient(180deg,var(--blue),var(--blue-light))}

.account-tab{position:absolute;top:0;width:43px;height:94px;border-radius:0 0 5px 5px;display:flex;align-items:center;justify-content:center}
.account-tab span{transform:rotate(-90deg);white-space:nowrap;font-weight:700;font-size:15px}
.account-tab.login{left:969px;background:#e8e8e8;color:#333;border:1px solid #ccc}
.account-tab.signup{left:1019px;background:#111;color:#fff}

.board-bar{position:absolute;left:71px;top:139px;width:989px;height:47px;border-radius:5px 5px 0 0;background:linear-gradient(180deg,var(--bar-mid),var(--bar-dark));display:flex;align-items:center}
.following{position:relative;width:127px;height:47px;background:linear-gradient(180deg,#fafafa,#dcdcdc);border-radius:5px 0 0 0;padding:13px 0 0 30px;font-size:12px;line-height:13px;color:#222}
.following b{display:block}
.following::after{content:"";position:absolute;right:-13px;top:0;border-left:13px solid #e8e8e8;border-top:23.5px solid transparent;border-bottom:23.5px solid transparent}
.board-link{color:#fff;font-size:11px;padding:0 36px;height:27px;display:flex;align-items:center;border-right:1px solid #777}
.board-link:first-of-type{padding-left:45px}
.board-link.last{border-right:none}
.search{position:absolute;right:12px;top:12px;width:216px;height:26px;background:#fff;border-radius:6px;display:flex;align-items:center;justify-content:space-between;padding:0 8px 0 18px;color:#aaa;font-size:14px}

.board{position:absolute;top:219px;left:71px;display:flex;gap:15px;align-items:flex-start}
.column{width:236px;display:flex;flex-direction:column;gap:18px}

.profile-card{position:relative;height:122px;background:linear-gradient(180deg,var(--red),var(--red-light));border:1px solid #d82a2a;color:#fff;padding:20px 0 0 24px}
.profile-card h2{font-size:17px;font-weight:700}
.profile-card .handle{font-size:24px;font-weight:700;margin-top:8px}
.profile-stats{display:flex;align-items:center;font-size:14px;margin-top:10px;gap:8px}
.profile-stats .divider{width:1px;height:20px;background:#fff;opacity:.7;margin:0 4px}
.add-btn{position:absolute;left:-25px;width:25px;height:28px;border-radius:5px 0 0 5px;color:#fff;font-weight:700;font-size:18px;display:flex;align-items:center;justify-content:center}
.add-btn.green{top:0;background:var(--green-light)}
.add-btn.blue{top:30px;background:var(--blue-light)}

.card{background:#fff;border:1px solid var(--card-border);border-radius:0 0 14px 0;overflow:hidden}
.card-media{position:relative}
.star-badge{position:absolute;right:0;bottom:0;width:30px;height:30px;background:rgba(40,40,40,.85);display:flex;align-items:center;justify-content:center}
.card-body{position:relative;padding:18px 40px 16px 19px}
.card-body h3{font-size:16px;font-weight:400;letter-spacing:.3px;color:#111}
.card-body p{font-size:11.5px;line-height:19px;color:var(--muted);margin-top:12px}
.card-actions{position:absolute;right:6px;top:12px;display:flex;flex-direction:column;gap:7px}
.card-actions i{display:flex;width:17px;height:17px;background:var(--icon);align-items:center;justify-content:center}
.category{height:19px;margin:0 0 -1px 0;background:linear-gradient(90deg,var(--red),var(--red-light));color:#fff;font-size:11.5px;padding:3px 0 0 19px;border-radius:0 0 14px 0}

.to-top{position:absolute;left:1076px;top:902px;width:29px;height:47px;background:#555;clip-path:polygon(50% 0,100% 22%,100% 100%,0 100%,0 22%);display:flex;align-items:center;justify-content:center}
.to-top span{transform:rotate(-90deg);color:#fff;font-size:11px;font-weight:700;margin-top:8px}
.loader{position:absolute;left:543px;top:1110px}
</style>
</head>
<body>
<div class="top-stripe"></div>

<header class="site-header">
  <div class="brand"><span class="brand-name">Kornr.me</span></div>
  <nav class="section-tabs">
    <div class="section-tab red">My Home Page</div>
    <div class="section-tab green">My Favorites Videos</div>
    <div class="section-tab blue">Personal Apps</div>
  </nav>
  <div class="account-tab login"><span>Log in</span></div>
  <div class="account-tab signup"><span>Sign up</span></div>

  <div class="board-bar">
    <div class="following"><b>Following</b>Kornr</div>
    <span class="board-link">Dovs Favorite Videos</span>
    <span class="board-link">Yaelis Pics + Links</span>
    <span class="board-link last">Family Weekly Calendar &amp; Notes</span>
    <div class="search">Search
      <svg width="15" height="15" viewBox="0 0 15 15"><circle cx="6" cy="6" r="4.5" fill="none" stroke="#555" stroke-width="2"/><line x1="9.5" y1="9.5" x2="13.5" y2="13.5" stroke="#555" stroke-width="2.2" stroke-linecap="round"/></svg>
    </div>
  </div>
</header>

<main class="board">
  <section class="column">
    <div class="profile-card">
      <span class="add-btn green">+</span><span class="add-btn blue">+</span>
      <h2>My Home Page</h2>
      <div class="handle">@Talvi07</div>
      <div class="profile-stats">
        <svg width="18" height="18" viewBox="0 0 24 24"><path fill="#fff" d="M12 2l3 7h7l-5.6 4.4 2.1 7.6L12 16.6 5.5 21l2.1-7.6L2 9h7z"/></svg>
        <span>1504</span><span class="divider"></span><span>Followers &nbsp; 99</span>
      </div>
    </div>
    <article class="card">
      <div class="card-media" role="img" aria-label="Two glass bottles raised against a golden sunset" style="height:346px;background:linear-gradient(180deg,#f7d27a,#e88a4a 45%,#7a3d24)">
        <span class="star-badge"><svg width="18" height="18" viewBox="0 0 24 24"><path fill="#fff" d="M12 2l3 7h7l-5.6 4.4 2.1 7.6L12 16.6 5.5 21l2.1-7.6L2 9h7z"/></svg></span>
      </div>
      <div class="card-body">
        <h3>Cancun, Mexico</h3>
        <p>Lorem ipsum dolor sit amet, consectetur adipiscing elit, sed do eiusmod tempor incididunt.</p>
        <div class="card-actions"><i></i><i></i></div>
      </div>
      <div class="category">Travel</div>
    </article>
  </section>

  <section class="column">
    <article class="card" style="margin-top:1px">
      <div class="card-media" role="img" aria-label="Colourful psychedelic illustration with swirling shapes" style="height:193px;background:linear-gradient(135deg,#e6557a,#f0a040 40%,#3a6fb0 70%,#555)">
        <span class="star-badge"><svg width="18" height="18" viewBox="0 0 24 24"><path fill="#fff" d="M12 2l3 7h7l-5.6 4.4 2.1 7.6L12 16.6 5.5 21l2.1-7.6L2 9h7z"/></svg></span>
      </div>
      <div class="card-body">
        <h3>New Art Blitz!</h3>
        <p>Art Blitz ideas and activities for adults that allow you to create your own Blitzes!</p>
        <div class="card-actions"><i></i><i></i></div>
      </div>
      <div class="category">Art</div>
    </article>
    <article class="card">
      <div class="card-media" role="img" aria-label="Rusty red hot rod truck parked outdoors" style="height:124px;background:linear-gradient(180deg,#5f8a48,#7a3a2c 50%,#4a4a4a)">
        <span class="star-badge"><svg width="18" height="18" viewBox="0 0 24 24"><path fill="#fff" d="M12 2l3 7h7l-5.6 4.4 2.1 7.6L12 16.6 5.5 21l2.1-7.6L2 9h7z"/></svg></span>
      </div>
      <div class="card-body">
        <h3>Hot Rod</h3>
        <p>Lorem ipsum dolor sit amet, consectetur adipiscing elit, sed do eiusmod tempor incididunt.</p>
        <div class="card-actions"><i></i><i></i></div>
      </div>
      <div class="category">Cars</div>
    </article>
    <article class="card">
      <div class="card-body">
        <h3>Seeker Spyder</h3>
        <p>Lorem ipsum dolor sit amet, consectetur adipiscing elit, sed do eiusmod tempor incididunt.</p>
        <div class="card-actions"><i><svg width="12" height="12" viewBox="0 0 24 24"><path fill="#fff" d="M12 2l3 7h7l-5.6 4.4 2.1 7.6L12 16.6 5.5 21l2.1-7.6L2 9h7z"/></svg></i><i></i><i></i></div>
      </div>
      <div class="category">News</div>
    </article>
  </section>

  <section class="column">
    <article class="card" style="margin-top:1px">
      <div class="card-media" role="img" aria-label="Portrait splashed with orange and blue paint" style="height:138px;background:linear-gradient(90deg,#e8e8e8,#f08a3a 40%,#3ab8e0 70%,#e8e8e8)">
        <span class="star-badge"><svg width="18" height="18" viewBox="0 0 24 24"><path fill="#fff" d="M12 2l3 7h7l-5.6 4.4 2.1 7.6L12 16.6 5.5 21l2.1-7.6L2 9h7z"/></svg></span>
      </div>
      <div class="card-body">
        <h3>Photoshooting</h3>
        <p>Lorem ipsum dolor sit amet, consectetur adipiscing elit, sed do eiusmod tempor incididunt.</p>
        <div class="card-actions"><i></i><i></i></div>
      </div>
      <div class="category">Photos</div>
    </article>
    <article class="card">
      <div class="card-body">
        <h3>Friendwall</h3>
        <p>Lorem ipsum dolor sit amet, consectetur adipiscing elit, sed do eiusmod tempor incididunt.</p>
        <div class="card-actions"><i><svg width="12" height="12" viewBox="0 0 24 24"><path fill="#fff" d="M12 2l3 7h7l-5.6 4.4 2.1 7.6L12 16.6 5.5 21l2.1-7.6L2 9h7z"/></svg></i><i></i><i></i></div>
      </div>
      <div class="category">News</div>
    </article>
    <article class="card">
      <div class="card-media" role="img" aria-label="Dark illustration of two monsters wearing 3D glasses in a red cinema" style="height:254px;background:radial-gradient(circle at 50% 45%,#c43040,#5a1a24 45%,#000 80%)">
        <span class="star-badge" style="background:none"><svg width="18" height="18" viewBox="0 0 24 24"><path fill="#fff" d="M12 2l3 7h7l-5.6 4.4 2.1 7.6L12 16.6 5.5 21l2.1-7.6L2 9h7z"/></svg></span>
      </div>
      <div class="card-body">
        <h3>3D</h3>
        <p>Lorem ipsum dolor sit amet, consectetur adipiscing elit, sed do eiusmod tempor incididunt.</p>
        <div class="card-actions"><i></i><i></i></div>
      </div>
      <div class="category">Illustration</div>
    </article>
  </section>

  <section class="column">
    <article class="card" style="margin-top:2px">
      <div class="card-body">
        <h3>Cyber Monday</h3>
        <p>Lorem ipsum dolor sit amet, consectetur adipiscing elit, sed do eiusmod tempor incididunt.</p>
        <div class="card-actions"><i><svg width="12" height="12" viewBox="0 0 24 24"><path fill="#fff" d="M12 2l3 7h7l-5.6 4.4 2.1 7.6L12 16.6 5.5 21l2.1-7.6L2 9h7z"/></svg></i><i></i><i></i></div>
      </div>
      <div class="category">News</div>
    </article>
    <article class="card">
      <div class="card-media" role="img" aria-label="Band performing on a stage under bright lights" style="height:148px;background:linear-gradient(180deg,#3a2a6a,#c04aa0 40%,#1a1a2a)">
        <span class="star-badge" style="background:none"><svg width="18" height="18" viewBox="0 0 24 24"><path fill="#fff" d="M12 2l3 7h7l-5.6 4.4 2.1 7.6L12 16.6 5.5 21l2.1-7.6L2 9h7z"/></svg></span>
      </div>
      <div class="card-body">
        <h3>Mirage</h3>
        <p>Lorem ipsum dolor sit amet, consectetur adipiscing elit, sed do eiusmod tempor incididunt.</p>
        <div class="card-actions"><i></i><i></i></div>
      </div>
      <div class="category">Music</div>
    </article>
    <article class="card">
      <div class="card-media" role="img" aria-label="Monkey sitting on a rocky shore by the sea" style="height:148px;background:linear-gradient(180deg,#8fb0cc,#9aa6a8 45%,#5a4a3a)">
        <span class="star-badge" style="background:none"><svg width="18" height="18" viewBox="0 0 24 24"><path fill="#fff" d="M12 2l3 7h7l-5.6 4.4 2.1 7.6L12 16.6 5.5 21l2.1-7.6L2 9h7z"/></svg></span>
      </div>
      <div class="card-body">
        <h3>Macau Island</h3>
        <p>Lorem ipsum dolor sit amet, consectetur adipiscing elit, sed do eiusmod tempor incididunt.</p>
        <div class="card-actions"><i></i><i></i></div>
      </div>
      <div class="category">Cultural</div>
    </article>
  </section>
</main>

<div class="to-top"><span>TOP</span></div>

<svg class="loader" width="42" height="42" viewBox="0 0 42 42" aria-label="Loading">
  <circle cx="21" cy="5" r="4" fill="#555"/>
  <circle cx="32" cy="10" r="3.4" fill="#666"/>
  <circle cx="37" cy="21" r="2" fill="#888"/>
  <circle cx="32" cy="32" r="2" fill="#888"/>
  <circle cx="21" cy="37" r="2.5" fill="#777"/>
  <circle cx="10" cy="32" r="3" fill="#666"/>
  <circle cx="5" cy="21" r="3.6" fill="#555"/>
  <circle cx="10" cy="10" r="4" fill="#555"/>
</svg>
</body>
</html>
```